New Business Cards for Velmora

About Velmora:
At Velmora, we're more than just a company—we're a force for positive change in the staffing industry. Our brand is our heartbeat, and we need a designer who can translate that into every design element.

The Project:
We're revamping our business cards and need your artistic flair to make them stand out. Here's what we're looking for:

- Incorporate our existing brand elements (logo, colours, fonts) into the design.
- Craft a design that's sleek, professional, and memorable.
- Provide options for different layouts and finishes.
- Collaborate closely with our team to ensure the final product exceeds expectations.

Please note: For general text, we use Avenir. The brand guidelines are slightly out of date and don't have correct imaging. Colours are correct though.

```html
<!DOCTYPE html>
<html lang="en">
<head>
<meta charset="utf-8">
<title>Velmora Business Cards</title>
<link href="https://fonts.googleapis.com/css2?family=Lato:wght@400;700;900&display=swap" rel="stylesheet">
<style>
  :root {
    --backdrop: #2b2b2e;
    --card-purple: #4d1458;
    --accent-pink: #ec107a;
    --text-light: #ffffff;
    --text-soft: #e9dcef;
  }
  * { margin: 0; padding: 0; box-sizing: border-box; }
  html, body {
    width: 1200px; height: 952px; overflow: hidden;
    background: var(--backdrop);
    font-family: "Lato", "Helvetica Neue", Arial, sans-serif;
  }
  .canvas {
    position: relative; width: 1200px; height: 952px;
    display: flex; align-items: center; justify-content: center; gap: 50px;
  }
  .card {
    position: relative; width: 530px; height: 303px;
    background: var(--card-purple);
    border-radius: 22px; overflow: hidden;
    box-shadow: 0 18px 40px rgba(0,0,0,.45);
    color: var(--text-light);
  }

  .wordmark { display: flex; flex-direction: column; }
  .wordmark-name {
    font-weight: 900; font-size: 40px; letter-spacing: -0.5px; line-height: 1;
    color: var(--text-light);
  }
  .wordmark-tagline {
    font-weight: 400; font-size: 11px; color: var(--text-soft);
    margin-top: 6px; letter-spacing: .3px;
  }

  /* Contact side */
  .contact-card .wordmark {
    position: absolute; left: 48px; top: 38px; align-items: flex-start;
  }
  .contact-list {
    position: absolute; left: 48px; top: 130px;
    list-style: none; font-size: 13px; line-height: 1.35; color: var(--text-soft);
  }
  .contact-list li { display: flex; align-items: flex-start; gap: 10px; margin-bottom: 7px; }
  .contact-icon {
    flex: none; width: 16px; height: 16px; border-radius: 3px;
    background: var(--text-light);
    display: flex; align-items: center; justify-content: center;
    margin-top: 1px;
  }
  .contact-icon.is-accent { background: var(--accent-pink); }
  .contact-icon svg { width: 11px; height: 11px; }

  .person {
    position: absolute; right: 40px; top: 120px; text-align: right;
  }
  .person-name {
    font-size: 21px; letter-spacing: .5px; color: var(--accent-pink);
    font-weight: 400; text-transform: uppercase; white-space: nowrap;
  }
  .person-name strong { font-weight: 900; }
  .person-title { font-size: 16px; color: var(--text-light); margin-top: 3px; }

  .pink-tab { position: absolute; background: var(--accent-pink); border-radius: 8px; }
  .contact-card .pink-tab { right: 18px; bottom: -8px; width: 150px; height: 24px; }

  /* Brand side */
  .brand-card .wordmark {
    position: absolute; left: 0; right: 0; top: 108px; align-items: center;
  }
  .brand-card .wordmark-name { font-size: 62px; }
  .brand-card .wordmark-tagline { font-size: 15px; margin-top: 8px; }
  .brand-card .pink-tab.top { left: 70px; top: -8px; width: 150px; height: 26px; }
  .brand-card .pink-tab.bottom { right: 70px; bottom: -8px; width: 150px; height: 26px; }
</style>
</head>
<body>
<main class="canvas">

  <section class="card contact-card" aria-label="Business card, contact side">
    <div class="wordmark">
      <div class="wordmark-name">Velmora</div>
      <div class="wordmark-tagline">people first, always</div>
    </div>

    <ul class="contact-list">
      <li>
        <span class="contact-icon is-accent">
          <svg viewBox="0 0 12 12"><path d="M6 1a3.5 3.5 0 0 0-3.5 3.5C2.5 7 6 11 6 11s3.5-4 3.5-6.5A3.5 3.5 0 0 0 6 1zm0 4.8a1.3 1.3 0 1 1 0-2.6 1.3 1.3 0 0 1 0 2.6z" fill="#fff"/></svg>
        </span>
        <span>2175 Maple Ridge Avenue<br>Portland, OR 97205</span>
      </li>
      <li>
        <span class="contact-icon">
          <svg viewBox="0 0 12 12"><path d="M3 1.5l1.6 2.2-.9 1.1a6 6 0 0 0 3.5 3.5l1.1-.9 2.2 1.6-.9 1.6C6 10.4 1.6 6 1.4 2.4z" fill="#4d1458"/></svg>
        </span>
        <span>+00 321 654 90</span>
      </li>
      <li>
        <span class="contact-icon">
          <svg viewBox="0 0 12 12"><rect x="1.5" y="3" width="9" height="6.5" rx="1" fill="none" stroke="#4d1458" stroke-width="1.3"/><path d="M1.8 3.4L6 6.8l4.2-3.4" fill="none" stroke="#4d1458" stroke-width="1.3"/></svg>
        </span>
        <span>hello@velmora.com</span>
      </li>
      <li>
        <span class="contact-icon">
          <svg viewBox="0 0 12 12"><circle cx="6" cy="6" r="4.3" fill="none" stroke="#4d1458" stroke-width="1.2"/><path d="M1.7 6h8.6M6 1.7c-2 2.6-2 6 0 8.6M6 1.7c2 2.6 2 6 0 8.6" fill="none" stroke="#4d1458" stroke-width="1"/></svg>
        </span>
        <span>www.velmora.com</span>
      </li>
    </ul>

    <div class="person">
      <div class="person-name">Daniel R. <strong>Hartwell</strong></div>
      <div class="person-title">Managing Director</div>
    </div>

    <span class="pink-tab"></span>
  </section>

  <section class="card brand-card" aria-label="Business card, brand side">
    <span class="pink-tab top"></span>
    <div class="wordmark">
      <div class="wordmark-name">Velmora</div>
      <div class="wordmark-tagline">people first, always</div>
    </div>
    <span class="pink-tab bottom"></span>
  </section>

</main>
</body>
</html>
```